Larkmoor Counseling

We need a postcard design for a Brooklyn based counseling service geared towards new parents. The postcard will be placed in pediatrician's offices, kids stores, and any place parents frequent. We would like to see designs that incorporate elements, fonts, textures, etc from the website (www.larkmoorcounseling.example) and some of the basic text used to describe the business.

I've included a copy of the logo, the font file we used to create the logo, and the main image from the index of the website, and the background texture.

Target Market(s)

New parents in Brooklyn.

Industry/Entity Type

Business

Requirements
Must have
• Contact info, website.
Should not have
• This postcard is for display and promotional purposes in doctor's offices and kid's toy/clothing stores.

It does not need an area for postage / address.

```html
<!DOCTYPE html>
<html lang="en">
<head>
<meta charset="utf-8">
<title>Larkmoor Counseling – Postcard</title>
<link rel="stylesheet" href="https://fonts.googleapis.com/css2?family=Open+Sans:ital,wght@0,300;0,400;0,700;1,400;1,700&family=Tinos&display=swap">
<style>
  :root {
    --page-bg: #5e5f61;
    --card-bg: #ffffff;
    --ink: #1d1d1b;
    --band: #231f20;
    --band-text: #ffffff;
    --footer-bg: #e9e6d2;
    --bullet: #c9a23c;
    --photo-warm: #e8d2b4;
    --photo-sky: #cfe0ea;
    --photo-green: #9fbf6a;
  }
  html, body {
    margin: 0;
    width: 1200px;
    height: 962px;
    overflow: hidden;
    background: var(--page-bg);
  }
  .postcard {
    position: absolute;
    left: 82px;
    top: 83px;
    width: 1036px;
    height: 795px;
    background: var(--card-bg);
    overflow: hidden;
    color: var(--ink);
    font-family: "Open Sans", Arial, sans-serif;
  }
  .family-photo {
    position: absolute;
    left: 330px;
    top: 142px;
    width: 706px;
    height: 483px;
    background:
      radial-gradient(ellipse at 95% 10%, var(--photo-green) 0%, transparent 30%),
      radial-gradient(ellipse at 55% 55%, var(--photo-warm) 0%, transparent 55%),
      radial-gradient(ellipse at 85% 60%, #d9cdb8 0%, transparent 45%),
      linear-gradient(90deg, #ffffff 0%, var(--photo-sky) 22%, #e6dccd 55%, #d8cbb5 100%);
  }
  .brand {
    position: absolute;
    left: 30px;
    top: 40px;
    display: flex;
    align-items: center;
    gap: 14px;
  }
  .brand-mark {
    width: 58px;
    height: 58px;
    border-radius: 50%;
    background: var(--ink);
  }
  .brand-name {
    font-family: "Open Sans", Arial, sans-serif;
    font-weight: 300;
    font-size: 56px;
    letter-spacing: 1px;
    text-transform: uppercase;
    line-height: 1;
    color: var(--ink);
  }
  .headline {
    position: absolute;
    left: 50px;
    top: 135px;
    margin: 0;
    font-family: "Tinos", "Times New Roman", serif;
    font-weight: 400;
    font-size: 47px;
    letter-spacing: 0.5px;
    line-height: 1;
  }
  .intro {
    position: absolute;
    left: 46px;
    top: 201px;
    width: 545px;
    margin: 0;
    font-style: italic;
    font-size: 18px;
    line-height: 26.5px;
  }
  .intro strong { font-weight: 700; }
  .focus {
    position: absolute;
    left: 46px;
    top: 411px;
    width: 320px;
  }
  .focus-title {
    margin: 0 0 10px;
    font-weight: 700;
    font-size: 18px;
  }
  .focus-list {
    list-style: none;
    margin: 0;
    padding: 0;
    font-size: 19px;
    line-height: 26px;
  }
  .focus-list li {
    position: relative;
    padding-left: 16px;
  }
  .focus-list li::before {
    content: "";
    position: absolute;
    left: 0;
    top: 9px;
    width: 9px;
    height: 9px;
    background: var(--bullet);
  }
  .tagline-band {
    position: absolute;
    left: 0;
    top: 625px;
    width: 100%;
    height: 40px;
    background: var(--band);
    color: var(--band-text);
    font-family: "Tinos", "Times New Roman", serif;
    font-size: 26px;
    line-height: 40px;
    text-align: center;
    letter-spacing: 0.3px;
  }
  .contact-footer {
    position: absolute;
    left: 0;
    top: 665px;
    width: 100%;
    height: 130px;
    background: var(--footer-bg);
  }
  .consult-note {
    position: absolute;
    left: 50px;
    top: 30px;
    width: 450px;
    margin: 0;
    text-align: center;
    font-weight: 700;
    font-style: italic;
    font-size: 21px;
    line-height: 31px;
    letter-spacing: 0.5px;
  }
  .phone {
    position: absolute;
    left: 585px;
    top: 22px;
    margin: 0;
    font-size: 38px;
    line-height: 1.2;
  }
  .email {
    position: absolute;
    left: 572px;
    top: 82px;
    margin: 0;
    font-size: 20px;
  }
</style>
</head>
<body>
  <main class="postcard">
    <div class="family-photo" role="img" aria-label="Photo of a smiling young family: mother, father and two small children hugging outdoors"></div>

    <header class="brand">
      <span class="brand-mark" aria-hidden="true"></span>
      <span class="brand-name">Larkmoor Counseling</span>
    </header>

    <h1 class="headline">IN-HOME THERAPY FOR PARENTS</h1>

    <p class="intro"><strong>Nora Whitfield</strong> is a licensed clinical social worker with years of experience working with pregnant women, new moms &amp; dads, and couples struggling through the early parenting years.Since even getting out of the house with a newborn can feel like a struggle, Nora Whitfield will meet with parents in their home for therapy sessions.</p>

    <section class="focus">
      <h2 class="focus-title">Therapy may focus on:</h2>
      <ul class="focus-list">
        <li>Pregnancy and postpartum depression</li>
        <li>Stress and anxiety</li>
        <li>Relationship changes</li>
        <li>Confidence building</li>
        <li>Balancing work and home life</li>
      </ul>
    </section>

    <div class="tagline-band">A COMPREHENSIVE PRACTICE FOR NEW AND EXPECTING PARENTS</div>

    <footer class="contact-footer">
      <p class="consult-note">FREE PHONE CONSULTATION AND TO<br>SCHEDULE AN INITIAL APPOINTMENT</p>
      <p class="phone">Call : 555.014.2870</p>
      <p class="email">Email : nora@larkmoorcounseling.example</p>
    </footer>
  </main>
</body>
</html>
```